Saffron Tram food box

To design a label (sticker) for my Biriyani and Curries that comply with Australian food labeling regulations for cook chilled food.

one sticker that covers all 4 sides of the box

```html
<!DOCTYPE html>
<html lang="en">
<head>
<meta charset="utf-8">
<title>Saffron Tram – Chicken Biriyani Box Label</title>
<link href="https://fonts.googleapis.com/css2?family=Open+Sans:wght@400;600;700&family=Bebas+Neue&family=Lobster&family=Libre+Franklin:wght@400;700;900&family=Oswald:wght@300;400&display=swap" rel="stylesheet">
<style>
  :root{
    --panel:#202020;
    --panel-edge:#2a2a2a;
    --green:#4cb847;
    --green-bright:#3fbf3a;
    --orange:#f39325;
    --orange-deep:#e86a1c;
    --grey-type:#a8a8a8;
    --grey-light:#cfcfcf;
    --text:#e8e8e8;
    --usebox:#717171;
    --white:#ffffff;
    --black:#000000;
    --seal-gold:#e9b52c;
    --seal-red:#b3141b;
  }
  *{box-sizing:border-box;margin:0;padding:0}
  html,body{width:685px;height:1200px;overflow:hidden;background:var(--white)}
  body{position:relative;font-family:'Open Sans',sans-serif;color:var(--text)}
  .panel{position:absolute;left:52px;width:578px;background:radial-gradient(ellipse at 50% 40%,var(--panel-edge),var(--panel) 70%)}
  .panel--back{top:52px;height:346px;overflow:hidden}
  .panel--front{top:400px;height:576px;overflow:hidden}
  .panel--side{top:978px;height:168px;overflow:hidden}
  .abs{position:absolute}

  /* back panel */
  .brand-small{left:18px;top:26px;display:flex;align-items:center;gap:6px;font-family:'Lobster',cursive;font-size:24px;color:var(--orange)}
  .brand-small .dot{width:14px;height:14px;border-radius:50%;background:var(--orange)}
  .section-title{font-weight:700;color:var(--green);font-size:13px;letter-spacing:.3px;white-space:nowrap}
  .ingredients{left:23px;top:83px;width:170px}
  .ingredients p{font-size:10.3px;line-height:12.3px;margin-top:13px}
  .ingredients p:first-of-type{margin-top:15px}
  .heating{left:201px;top:34px;width:200px}
  .heating .lead{font-size:10.3px;line-height:13px;margin-top:1px}
  .method{position:absolute;width:93px;font-size:7px;line-height:8.8px}
  .method .time{display:flex;align-items:flex-end;gap:5px;height:20px}
  .method .num{font-weight:700;font-size:12px;line-height:11px}
  .method .unit{display:block;font-size:6px;font-weight:600;line-height:7px}
  .method .label{font-weight:700;font-size:7px;border-bottom:.6px solid var(--orange);padding-bottom:1px;margin-bottom:1px;line-height:9px;white-space:nowrap}
  .m1{left:201px;top:82px}.m2{left:303px;top:82px}
  .m3{left:201px;top:202px}.m4{left:303px;top:202px}

  .nutrition{left:402px;top:37px;width:152px;height:282px;background:var(--white);color:var(--black);font-family:'Libre Franklin',sans-serif;padding:1px 3px 0}
  .nutrition h2{font-weight:900;font-size:17.5px;line-height:20px;border-bottom:.6px solid var(--black);white-space:nowrap}
  .nf-serv{font-size:8.5px;line-height:9.5px;margin-top:2px}
  .nf-serv b{font-weight:900;display:flex;justify-content:space-between}
  .bar-thick{height:6px;background:var(--black);margin:3px 0 3px}
  .bar-mid{height:3px;background:var(--black);margin:1px 0 2px}
  .nf-amt{font-size:5px;font-weight:900}
  .nf-cal{display:flex;justify-content:space-between;font-weight:900;font-size:14px;line-height:15px}
  .nf-dv{font-size:5.5px;font-weight:900;text-align:right;border-bottom:.5px solid var(--black);padding-bottom:1px}
  .nf-row{display:flex;justify-content:space-between;font-size:7.2px;line-height:10.6px;border-bottom:.5px solid var(--black)}
  .nf-row b{font-weight:900}
  .nf-row .pct{font-weight:900}
  .nf-row.in1{padding-left:9px}
  .nf-row.in2{padding-left:18px}
  .nf-row.nob{border-bottom:none}
  .nf-row.light .pct{font-weight:400}
  .nf-foot{font-size:4.8px;line-height:6.2px;padding:3px 2px 0}

  /* front panel */
  .brand-large{left:36px;top:52px;display:flex;align-items:center;gap:12px;font-family:'Lobster',cursive;font-size:46px;color:var(--orange)}
  .brand-large .dot{width:40px;height:40px;border-radius:50%;background:var(--orange)}
  .brand-rule{left:146px;top:132px;width:250px;height:4px;border-radius:2px;background:linear-gradient(90deg,transparent,var(--green))}
  .tagline{left:35px;top:160px;font-family:'Lobster',cursive;font-size:29px;color:var(--orange)}
  .dots{left:33px;top:199px;width:218px;border-top:3px dotted var(--green)}
  .dish{left:28px;top:208px;font-family:'Bebas Neue',sans-serif;color:var(--grey-type);font-size:82px;line-height:78px;letter-spacing:-1px;text-align:center;width:230px}
  .ornament{left:66px;top:359px;width:152px;height:26px;border-radius:13px;background:linear-gradient(90deg,transparent,#8d8d8d 30%,#8d8d8d 70%,transparent)}
  .blurb{left:28px;top:393px;width:230px;text-align:center;font-family:'Oswald',sans-serif;font-weight:300;font-size:11.4px;line-height:16.5px;color:var(--orange)}
  .seal{left:35px;top:454px;width:98px;height:98px;border-radius:50%;background:var(--seal-gold);display:flex;align-items:center;justify-content:center}
  .seal-inner{width:72px;height:72px;border-radius:50%;background:radial-gradient(circle at 45% 35%,#d8262a,var(--seal-red) 60%,#7d0d12);color:var(--white);text-align:center;font-weight:700;display:flex;flex-direction:column;justify-content:center;line-height:1}
  .seal-inner .s1{font-size:8px;letter-spacing:1px}
  .seal-inner .s2{font-size:28px;line-height:26px}
  .seal-inner .s3{font-size:9px;letter-spacing:.5px}
  .useby{left:148px;top:473px;width:136px;height:75px;background:var(--usebox);padding:4px 12px;font-family:'Oswald',sans-serif;font-size:14px;color:var(--black)}
  .photo{left:250px;top:130px;width:328px;height:350px}
  .served{left:406px;top:446px;font-family:'Oswald',sans-serif;font-size:13px;line-height:20px;color:var(--green);transform:rotate(-9deg);transform-origin:left top;text-transform:uppercase;white-space:nowrap}
  .claim{position:absolute;top:494px;width:64px;text-align:center;font-family:'Oswald',sans-serif;font-size:10.5px;color:var(--orange);white-space:nowrap}
  .claim .mark{display:block;width:39px;height:39px;border-radius:50%;background:var(--green-bright);margin:0 auto 6px;border:2px solid var(--white)}
  .claim.gf{left:295px}.claim.halal{left:357px}
  .weight{left:432px;top:512px;font-family:'Oswald',sans-serif;font-weight:400;font-size:36px;color:var(--grey-light);letter-spacing:1px}

  /* side panel */
  .illustration{left:33px;top:14px;width:146px;height:146px;border-radius:50%;background:radial-gradient(circle,#f6c944,#e25b24 65%,#c8981f)}
  .promise{left:206px;top:24px;font-family:'Oswald',sans-serif;font-size:20px;line-height:27px;letter-spacing:2px;color:var(--grey-light);text-transform:uppercase;white-space:nowrap}
  .promise .accent{color:var(--green-bright);letter-spacing:0}
  .others{left:206px;top:94px;width:152px;font-family:'Oswald',sans-serif;color:var(--grey-light);text-transform:uppercase;white-space:nowrap}
  .others .h{font-size:13px;line-height:17px;letter-spacing:1px}
  .others .list{font-size:10.5px;line-height:15px;letter-spacing:.6px}
  .dish-photo{position:absolute;top:80px;width:71px;height:71px;border-radius:50%;border:3px solid #8a4a2a}
  .dish-photo.veg{left:364px;background:radial-gradient(circle,#d9c28a,#8b6a3a)}
  .dish-photo.lamb{left:445px;background:radial-gradient(circle,#e0b34a,#8a6322)}
</style>
</head>
<body>

<section class="panel panel--back">
  <div class="abs brand-small"><span class="dot"></span>Saffron Tram</div>

  <div class="abs ingredients">
    <h3 class="section-title">INGREDIENTS LIST</h3>
    <p>In publishing and graphic design, Lorem ipsum is a placeholder text.</p>
    <p>In publishing and graphic design, Lorem ipsum is a placeholder text commonly used to demonstrate the visual form of a document or a typeface without relying on meaningful content. Lorem ipsum may be used as a placeholder before final copy is available.</p>
    <p>In publishing and graphic design, Lorem ipsum is a placeholder text used to demonstrate the visual form of a document or a typeface without relying on content.</p>
  </div>

  <div class="abs heating">
    <h3 class="section-title">HEATING INSTRUCTION</h3>
    <p class="lead">In publishing and graphic design,<br>Lorem ipsum is a placeholder text .</p>
  </div>

  <div class="method m1">
    <div class="time"><div><span class="num">04</span><span class="unit">MIN</span></div>
      <svg width="24" height="16" viewBox="0 0 24 16"><rect x="1" y="1" width="22" height="14" rx="1.5" fill="none" stroke="#f39325" stroke-width="2"/><rect x="4" y="4" width="11" height="8" fill="#f39325"/><rect x="17" y="4" width="4" height="2" fill="#f39325"/><rect x="17" y="8" width="4" height="2" fill="#f39325"/></svg></div>
    <div class="label">Microwave</div>
    1. in graphic design, Lorem ipsum is a placeholder.<br>2. in graphic design, Lorem ipsum is a placeholder.<br>3. in graphic design, Lorem ipsum is a placeholder.<br>4. in graphic design, Lorem ipsum is a placeholder.<br>5. in graphic design, Lorem ipsum is a placeholder.
  </div>
  <div class="method m2">
    <div class="time"><div><span class="num">20</span><span class="unit">MIN</span></div>
      <svg width="26" height="16" viewBox="0 0 26 16"><path d="M6 6 q1-3 0-5 M10 6 q1-3 0-5 M14 6 q1-3 0-5 M18 6 q1-3 0-5" stroke="#f39325" stroke-width="1.6" fill="none"/><rect x="2" y="7" width="22" height="3" fill="#f39325"/><rect x="4" y="10" width="18" height="6" rx="1" fill="#f39325"/><circle cx="13" cy="13" r="1.5" fill="#202020"/></svg></div>
    <div class="label">Oven</div>
    1. in graphic design, Lorem ipsum is a placeholder.<br>2. in graphic design, Lorem ipsum is a placeholder.<br>3. in graphic design, Lorem ipsum is a placeholder.<br>4. in graphic design, Lorem ipsum is a placeholder.<br>5. in graphic design, Lorem ipsum is a placeholder.
  </div>
  <div class="method m3">
    <div class="time"><div><span class="num">06</span><span class="unit">MIN</span></div>
      <svg width="24" height="16" viewBox="0 0 24 16"><rect x="1" y="1" width="22" height="14" rx="1.5" fill="none" stroke="#f39325" stroke-width="2"/><rect x="4" y="4" width="11" height="8" fill="#f39325"/><rect x="17" y="4" width="4" height="2" fill="#f39325"/><rect x="17" y="8" width="4" height="2" fill="#f39325"/></svg></div>
    <div class="label">Microwave ( from frozen )</div>
    1. in graphic design, Lorem ipsum is a placeholder.<br>2. in graphic design, Lorem ipsum is a placeholder.<br>3. in graphic design, Lorem ipsum is a placeholder.<br>4. in graphic design, Lorem ipsum is a placeholder.<br>5. in graphic design, Lorem ipsum is a placeholder.
  </div>
  <div class="method m4">
    <div class="time"><div><span class="num">45</span><span class="unit">MIN</span></div>
      <svg width="26" height="16" viewBox="0 0 26 16"><path d="M6 6 q1-3 0-5 M10 6 q1-3 0-5 M14 6 q1-3 0-5 M18 6 q1-3 0-5" stroke="#f39325" stroke-width="1.6" fill="none"/><rect x="2" y="7" width="22" height="3" fill="#f39325"/><rect x="4" y="10" width="18" height="6" rx="1" fill="#f39325"/><circle cx="13" cy="13" r="1.5" fill="#202020"/></svg></div>
    <div class="label">Oven ( from frozen )</div>
    1. in graphic design, Lorem ipsum is a placeholder.<br>2. in graphic design, Lorem ipsum is a placeholder.<br>3. in graphic design, Lorem ipsum is a placeholder.<br>4. in graphic design, Lorem ipsum is a placeholder.<br>5. in graphic design, Lorem ipsum is a placeholder.
  </div>

  <div class="abs nutrition">
    <h2>Nutrition Facts</h2>
    <div class="nf-serv">2 servings per container<b><span>Serving size</span><span>x/x cup (xxg)</span></b></div>
    <div class="bar-thick"></div>
    <div class="nf-amt">Amount per serving</div>
    <div class="nf-cal"><span>Calories</span><span>XXX</span></div>
    <div class="bar-mid"></div>
    <div class="nf-dv">% Daily Value*</div>
    <div class="nf-row"><span><b>Total Fat</b> xg</span><span class="pct">xx%</span></div>
    <div class="nf-row in1"><span>Saturated Fat xg</span><span class="pct">x%</span></div>
    <div class="nf-row in1"><span><i>Trans</i> Fat xg</span><span></span></div>
    <div class="nf-row"><span><b>Cholesterol</b> xmg</span><span class="pct">x%</span></div>
    <div class="nf-row"><span><b>Sodium</b> xxmg</span><span class="pct">x%</span></div>
    <div class="nf-row"><span><b>Total Carbohydrate</b> xxg</span><span class="pct">xx%</span></div>
    <div class="nf-row in1"><span>Dietary Fiber xg</span><span class="pct">xx%</span></div>
    <div class="nf-row in1"><span>Total Sugars xxg</span><span></span></div>
    <div class="nf-row in2"><span>Includes xxg Added Sugars</span><span class="pct">xx%</span></div>
    <div class="nf-row nob"><span><b>Protein</b> xxg</span><span></span></div>
    <div class="bar-thick" style="margin:0 0 1px"></div>
    <div class="nf-row light"><span>Vitamin D xmcg</span><span class="pct">xx%</span></div>
    <div class="nf-row light"><span>Calcium xxxmg</span><span class="pct">xx%</span></div>
    <div class="nf-row light"><span>Iron xmg</span><span class="pct">xx%</span></div>
    <div class="nf-row light"><span>Potassium xxxmg</span><span class="pct">x%</span></div>
    <p class="nf-foot">* The % Daily Value (DV) tells you how much a nutrient in a serving of food contributes to a daily diet. 2,000 calories a day is used for general nutrition advice.</p>
  </div>
</section>

<section class="panel panel--front">
  <div class="abs brand-large"><span class="dot"></span>Saffron Tram</div>
  <div class="abs brand-rule"></div>

  <div class="abs tagline">Authentic Mughlai</div>
  <div class="abs dots"></div>
  <h1 class="abs dish">CHICKEN<br>BIRIYANI</h1>
  <div class="abs ornament" role="img" aria-label="Decorative scroll flourish divider"></div>
  <p class="abs blurb">LOREM IPSUM DOLOR SIT AMET, CONSECTETUER ADIPISCING ELIT, SED DIAM NONUMMY NIBH EUISMOD TINCIDUNT UT LAOREET DOLORE MAGNA ALIQUAM ERAT.</p>

  <svg class="abs photo" viewBox="0 0 328 350" role="img" aria-label="Photo of chicken biryani in a clay bowl with a bowl of raita and a bowl of salad">
    <defs>
      <radialGradient id="rice" cx="50%" cy="50%" r="50%"><stop offset="0" stop-color="#d9a24a"/><stop offset=".8" stop-color="#c88938"/><stop offset="1" stop-color="#a0512c"/></radialGradient>
      <radialGradient id="raita" cx="50%" cy="45%" r="50%"><stop offset="0" stop-color="#f4f4ee"/><stop offset=".75" stop-color="#dfe6dc"/><stop offset="1" stop-color="#b0643a"/></radialGradient>
      <radialGradient id="salad" cx="50%" cy="50%" r="50%"><stop offset="0" stop-color="#6ea53a"/><stop offset=".75" stop-color="#c0432d"/><stop offset="1" stop-color="#a65a34"/></radialGradient>
    </defs>
    <circle cx="192" cy="152" r="139" fill="url(#rice)"/>
    <circle cx="48" cy="237" r="33" fill="url(#raita)"/>
    <circle cx="103" cy="304" r="42" fill="url(#salad)"/>
  </svg>

  <p class="abs served">The biryani box is sold<br>with raita and salad</p>

  <div class="abs seal"><div class="seal-inner"><span class="s1">ENJOY IN</span><span class="s2">5</span><span class="s3">MINS</span></div></div>
  <div class="abs useby">USE BY:</div>

  <div class="claim gf"><span class="mark"></span>GLUTEN FREE</div>
  <div class="claim halal"><span class="mark"></span>HALAL</div>
  <div class="abs weight">600 GM</div>
</section>

<section class="panel panel--side">
  <div class="abs illustration" role="img" aria-label="Ornate circular illustration of a woman in traditional dress holding a serving pot"></div>
  <p class="abs promise">This biryani is made with love,<br><span class="accent">and 32 spices, herbs and essences</span></p>
  <div class="abs others"><p class="h">Try our other dishes:</p><p class="list">Veg Biryani / Lamb Biryani</p></div>
  <div class="dish-photo veg" role="img" aria-label="Photo of vegetable biryani in a bowl"></div>
  <div class="dish-photo lamb" role="img" aria-label="Photo of lamb biryani in a bowl"></div>
</section>

</body>
</html>
```